Candidate Table Page

Need our intranet page redesigned. The layout is perfect and doesn't need to change. But the whole page doesn't seem to fit well together. Please change the font, feel, and table borders to make a more professional and easy user interface. symbols and/or icons are okay.

Target Market(s)

company staff

Industry/Entity Type

Security Guard

Coding

Coded - Design and coding required

Number of Pages Required

1 page

Font styles to use
Sans Serif

Colors
0255a3
fece3e

Requirements
Must have
• the employee information and columns
Nice to have
• icons and maybe symbols.

```html
<!DOCTYPE html>
<html lang="en">
<head>
<meta charset="utf-8">
<title>Candidates</title>
<link href="https://fonts.googleapis.com/css2?family=Roboto:wght@400;500;700&display=swap" rel="stylesheet">
<style>
:root{
  --blue:#0255a3;
  --gold:#fece3e;
  --text:#444;
  --line:#dcdcdc;
  --bg:#f2f2f2;
}
*{box-sizing:border-box;margin:0;padding:0}
html,body{width:1200px;height:928px;overflow:hidden}
body{font-family:'Roboto',sans-serif;background:var(--bg);color:var(--text);position:relative;font-size:11.5px}
.topbar{position:absolute;left:0;top:0;width:1200px;height:78px;background:linear-gradient(#fbfbfb,#e3e3e3)}
.brand{position:absolute;left:0;top:0;width:194px;height:78px;background:#fff;display:flex;align-items:center;gap:8px;padding-left:12px;box-shadow:2px 2px 6px rgba(0,0,0,.12)}
.brand-mark{width:30px;height:30px;border-radius:50%;background:var(--blue);flex:none}
.brand-name{color:#f0b323;font-weight:700;font-size:15px;line-height:16px;text-transform:uppercase}
.search-label{position:absolute;left:236px;top:33px;font-size:11.5px;color:#555;font-weight:500}
.field{position:absolute;top:26px;height:27px;background:#fff;border:1px solid #cfcfcf;font-size:11px;color:#555;padding:0 9px;display:flex;align-items:center;justify-content:space-between}
.field .caret{width:0;height:0;border-left:4px solid transparent;border-right:4px solid transparent;border-top:5px solid #555}
.btn{position:absolute;top:26px;height:27px;color:#fff;font-size:11px;font-weight:500;display:flex;align-items:center;justify-content:center}
.btn-find{left:572px;width:63px;background:var(--blue)}
.btn-reset{left:641px;width:63px;background:var(--gold)}
.user{position:absolute;left:1082px;top:33px;font-size:11.5px;color:#444}
.power{position:absolute;left:1156px;top:22px;width:36px;height:36px;border-radius:50%;background:var(--blue)}
.power svg{position:absolute;left:9px;top:9px}
.sidenav{position:absolute;left:0;top:78px;width:192px;list-style:none}
.sidenav li{height:44.4px;background:var(--gold);border-bottom:1px solid rgba(255,255,255,.45);color:#fff;font-weight:700;font-size:11px;display:flex;align-items:center;justify-content:space-between;padding:0 14px 0 19px;text-transform:uppercase}
.sidenav .chev{width:6px;height:6px;border-right:1.5px solid #fff;border-bottom:1.5px solid #fff;transform:rotate(45deg);margin-top:-4px}
.panel{position:absolute;left:206px;top:102px;width:985px;background:#fff;border:1px solid var(--line)}
table{border-collapse:collapse;width:984px;table-layout:fixed}
thead th{background:var(--blue);color:#fff;font-weight:700;font-size:11px;text-align:left;height:48px;padding:0 9px;border-right:1px solid #3f7dbb}
thead th:last-child{border-right:none}
tbody td{height:52.5px;padding:0 9px;border-right:1px solid var(--line);border-bottom:1px solid var(--line);white-space:nowrap;overflow:hidden}
tbody td:last-child{border-right:none}
.pager{height:52px;display:flex;align-items:center;padding:0 12px}
.pg{height:23px;min-width:23px;border:1px solid #d5d5d5;background:#fafafa;display:flex;align-items:center;justify-content:center;font-weight:700;font-size:11px;color:#555;margin-right:7px;padding:0 6px}
.pg.wide{width:45px}
.pg.gap{color:#aaa;font-weight:400}
.size-label{margin:0 16px 0 6px;color:#555}
.size{width:68px;height:23px;border:1px solid #d5d5d5;display:flex;align-items:center;justify-content:space-between;padding:0 8px;color:#555}
.size .caret{width:0;height:0;border-left:4px solid transparent;border-right:4px solid transparent;border-top:5px solid #555}
.count{margin-left:auto;color:#555}
.count b{color:var(--blue);font-weight:400}
.footer{position:absolute;left:0;top:874px;width:1200px;height:54px;background:var(--blue);color:#fff;font-size:11px;display:flex;align-items:center;justify-content:center}
</style>
</head>
<body>
<header class="topbar">
  <div class="brand"><span class="brand-mark"></span><span class="brand-name">Sentinel Shield<br>Services</span></div>
  <span class="search-label">SEARCH BY :</span>
  <div class="field" style="left:307px;width:120px">Name :<span class="caret"></span></div>
  <div class="field" style="left:431px;width:136px"></div>
  <div class="btn btn-find">FIND</div>
  <div class="btn btn-reset">RESET</div>
  <div class="field" style="left:708px;width:113px">Job :<span class="caret"></span></div>
  <div class="field" style="left:828px;width:113px">Status :<span class="caret"></span></div>
  <div class="field" style="left:947px;width:113px">Office :<span class="caret"></span></div>
  <span class="user">Omar Haddad</span>
  <div class="power"><svg width="18" height="18" viewBox="0 0 18 18"><path d="M5.5 5.2a5 5 0 1 0 7 0" fill="none" stroke="#fff" stroke-width="1.8" stroke-linecap="round"/><line x1="9" y1="3" x2="9" y2="9" stroke="#fff" stroke-width="1.8" stroke-linecap="round"/></svg></div>
</header>

<ul class="sidenav">
  <li>Home</li>
  <li>Human Resource<span class="chev"></span></li>
  <li>Recruiting<span class="chev"></span></li>
  <li>Inventory<span class="chev"></span></li>
  <li>Contracts<span class="chev"></span></li>
  <li>Supervision<span class="chev"></span></li>
  <li>Reports<span class="chev"></span></li>
  <li>Settings<span class="chev"></span></li>
  <li>Organisation Chart</li>
</ul>

<main class="panel">
  <table class="candidates">
    <colgroup>
      <col style="width:80px"><col style="width:103px"><col style="width:90px"><col style="width:91px"><col style="width:119px"><col style="width:65px"><col style="width:64px"><col style="width:69px"><col style="width:68px"><col style="width:71px"><col style="width:65px"><col style="width:99px">
    </colgroup>
    <thead>
      <tr><th>Created</th><th>Name</th><th>Phone</th><th>Call</th><th>City State</th><th>Status</th><th>Note</th><th>Reason</th><th>Reactivate</th><th>Retest</th><th>Rehire</th><th>Job Position</th></tr>
    </thead>
    <tbody>
      <tr><td>23-Jun-2017</td><td>Aaron Pike</td><td>(555)-201-4417</td><td>(555)-310-2284</td><td>Hesperia California</td><td>Qualified</td><td>Notes</td><td></td><td></td><td></td><td></td><td>UN-Armed Guard</td></tr>
      <tr><td>23-Jun-2017</td><td>Wes Warner</td><td>(555)-201-4417</td><td>(555)-310-2284</td><td>Hesperia California</td><td>Qualified</td><td>Notes</td><td></td><td></td><td></td><td></td><td>UN-Armed Guard</td></tr>
      <tr><td>23-Jun-2017</td><td>Anita Sole</td><td>(555)-201-4417</td><td>(555)-310-2284</td><td>Hesperia California</td><td>Qualified</td><td>Notes</td><td></td><td></td><td></td><td></td><td>UN-Armed Guard</td></tr>
      <tr><td>23-Jun-2017</td><td>Bianca Joy Hale</td><td>(555)-201-4417</td><td>(555)-310-2284</td><td>Hesperia California</td><td>Qualified</td><td>Notes</td><td></td><td></td><td></td><td></td><td>UN-Armed Guard</td></tr>
      <tr><td>23-Jun-2017</td><td>Ralph Jensen</td><td>(555)-201-4417</td><td>(555)-310-2284</td><td>Hesperia California</td><td>Qualified</td><td>Notes</td><td></td><td></td><td></td><td></td><td>UN-Armed Guard</td></tr>
      <tr><td>23-Jun-2017</td><td>Jason Brandt</td><td>(555)-201-4417</td><td>(555)-310-2284</td><td>Hesperia California</td><td>Qualified</td><td>Notes</td><td></td><td></td><td></td><td></td><td>UN-Armed Guard</td></tr>
      <tr><td>23-Jun-2017</td><td>Dana Rowe</td><td>(555)-201-4417</td><td>(555)-310-2284</td><td>Hesperia California</td><td>Qualified</td><td>Notes</td><td></td><td></td><td></td><td></td><td>UN-Armed Guard</td></tr>
      <tr><td>23-Jun-2017</td><td>Amy Rena Holt</td><td>(555)-201-4417</td><td>(555)-310-2284</td><td>Hesperia California</td><td>Qualified</td><td>Notes</td><td></td><td></td><td></td><td></td><td>UN-Armed Guard</td></tr>
      <tr><td>23-Jun-2017</td><td>Trent Garvey</td><td>(555)-201-4417</td><td>(555)-310-2284</td><td>Hesperia California</td><td>Qualified</td><td>Notes</td><td></td><td></td><td></td><td></td><td>UN-Armed Guard</td></tr>
      <tr><td>23-Jun-2017</td><td>Aaron Pike</td><td>(555)-201-4417</td><td>(555)-310-2284</td><td>Hesperia California</td><td>Qualified</td><td>Notes</td><td></td><td></td><td></td><td></td><td>UN-Armed Guard</td></tr>
      <tr><td>23-Jun-2017</td><td>Aaron Pike</td><td>(555)-201-4417</td><td>(555)-310-2284</td><td>Hesperia California</td><td>Qualified</td><td>Notes</td><td></td><td></td><td></td><td></td><td>UN-Armed Guard</td></tr>
      <tr><td>23-Jun-2017</td><td>Aaron Pike</td><td>(555)-201-4417</td><td>(555)-310-2284</td><td>Hesperia California</td><td>Qualified</td><td>Notes</td><td></td><td></td><td></td><td></td><td>UN-Armed Guard</td></tr>
    </tbody>
  </table>
  <nav class="pager">
    <span class="pg wide">Prev</span>
    <span class="pg">1</span><span class="pg">2</span><span class="pg">3</span><span class="pg">4</span><span class="pg">5</span><span class="pg">6</span><span class="pg gap">…</span><span class="pg">15</span>
    <span class="pg wide">Next</span>
    <span class="size-label">Page Size :</span>
    <span class="size">15<span class="caret"></span></span>
    <span class="count"><b>3361</b> items in <b>225</b> pages</span>
  </nav>
</main>

<footer class="footer">© Copyright 2017 Sentinel Shield Services.All Rights Reserved</footer>
</body>
</html>
```